Business Card Design

My business is writing crime novels to entertain readers. I write legal thrillers and mysteries. I need a card for publishers, agents, other authors, and media.

Industry/Entity Type

Legal

Contact Information for Business Card

Paul Ostrander
www.ostranderthrillers.example
paulbostrander@mailbox.example
0064 27 5139427

```html
<!DOCTYPE html>
<html lang="en">
<head>
<meta charset="utf-8">
<title>Paul Ostrander — Business Card</title>
<link rel="stylesheet" href="https://fonts.googleapis.com/css2?family=Michroma&display=swap">
<style>
  :root {
    --page-bg: #1c1c1e;
    --card-black: #0b0e0f;
    --scene-dark: #101616;
    --scene-teal: #24393a;
    --band-red: #5e0b0e;
    --band-red-dark: #3c0608;
    --name-red: #c8141b;
    --ring-teal: #4f6e6b;
    --ring-dark: #1d2b2a;
    --portrait-grey: #8b8b8d;
    --contact-white: #e9eceb;
  }
  html, body {
    margin: 0;
    width: 1200px;
    height: 900px;
    overflow: hidden;
    background: var(--page-bg);
  }
  .card {
    position: absolute;
    left: 75px;
    top: 150px;
    width: 1050px;
    height: 600px;
    background: var(--card-black);
    overflow: hidden;
    box-shadow: 0 10px 40px rgba(0,0,0,0.6);
  }
  .card-backdrop {
    position: absolute;
    inset: 0;
    background: linear-gradient(90deg, var(--card-black) 0%, var(--scene-dark) 35%, var(--scene-teal) 55%, var(--scene-dark) 80%, var(--card-black) 100%);
  }
  .accent-band {
    position: absolute;
    left: 250px;
    top: 0;
    width: 140px;
    height: 100%;
    background: linear-gradient(180deg, var(--band-red) 0%, var(--band-red-dark) 100%);
  }
  .portrait-ring {
    position: absolute;
    left: 150px;
    top: 120px;
    width: 340px;
    height: 340px;
    border-radius: 50%;
    background: var(--ring-teal);
    box-shadow: 0 6px 20px rgba(0,0,0,0.7);
  }
  .portrait {
    position: absolute;
    inset: 20px;
    border-radius: 50%;
    background: var(--portrait-grey);
  }
  .contact {
    position: absolute;
    right: 110px;
    top: 105px;
    text-align: right;
    font-family: "Michroma", sans-serif;
    text-shadow: 1px 2px 2px #000;
  }
  .contact-name {
    margin: 0 0 40px;
    font-size: 31px;
    font-weight: 400;
    color: var(--name-red);
  }
  .contact-line {
    margin: 0;
    font-size: 20px;
    line-height: 1.35;
    color: var(--contact-white);
  }
  .contact-phone { font-size: 22px; }
</style>
</head>
<body>
  <div class="card">
    <div class="card-backdrop" role="img" aria-label="Background photograph in dark teal tones"></div>
    <div class="accent-band"></div>
    <div class="portrait-ring">
      <div class="portrait" role="img" aria-label="Portrait photograph of the author"></div>
    </div>
    <div class="contact">
      <h1 class="contact-name">Paul Ostrander</h1>
      <p class="contact-line">www.ostranderthrillers.example</p>
      <p class="contact-line">paulbostrander@mailbox.example</p>
      <p class="contact-line contact-phone">0064 27 5139427</p>
    </div>
  </div>
</body>
</html>
```